http://www.lanternfieldcollective.org/

would like someone to rebuild this -http://www.lanternfieldcollective.com/ to be more modern and more easily updated

Industry/Entity Type

Non Profit

Coding

Coded - Design and coding required

Colors

Designer to choose colors to be used in the design.

Requirements
Must have
• use of the logo, and a newer design for wordpress to be hosted on Azure and easily updated templates

```html
<!DOCTYPE html>
<html lang="en">
<head>
<meta charset="utf-8">
<title>Lanternfield Collective</title>
<link rel="stylesheet" href="https://fonts.googleapis.com/css2?family=Playfair+Display:wght@700&family=Source+Sans+3:wght@400;600&display=swap">
<style>
:root{
  --ink:#2b2a35;
  --plum:#2e2540;
  --plum-deep:#3a2e4a;
  --red:#c0182f;
  --sky:#a8ccd8;
  --mist:#f2f2f5;
  --muted:#6b6b75;
  --btn-top:#70708a;
  --btn-bot:#2c2a42;
  --white:#fff;
  --serif:"Playfair Display",Georgia,serif;
  --sans:"Source Sans 3",Arial,sans-serif;
}
*{box-sizing:border-box;margin:0;padding:0}
html,body{width:1200px;height:3358px;overflow:hidden}
body{position:relative;background:var(--white);font-family:var(--sans);color:var(--ink)}
.abs{position:absolute}
.btn{position:absolute;display:flex;align-items:center;justify-content:center;border-radius:20px;font-size:14px;color:var(--white);background:linear-gradient(var(--btn-top),var(--btn-bot));text-decoration:none}
.btn-outline{background:var(--white);color:var(--ink);border:1.5px solid var(--btn-bot)}
h2{font-family:var(--serif);font-weight:700;color:var(--ink)}
.section-title{position:absolute;left:0;width:1200px;text-align:center;font-size:31px}

/* header */
.header-block{left:1050px;top:0;width:150px;height:238px;background:var(--plum)}
.brand{left:176px;top:20px;display:flex;align-items:center;gap:10px;font-family:var(--serif);font-size:20px;font-weight:700;color:var(--plum)}
.brand-dot{width:40px;height:40px;border-radius:50%;background:var(--plum)}
.donate{left:891px;top:13px;width:136px;height:37px;background:var(--red);font-weight:600;font-size:15px;border-radius:20px}
.nav{left:636px;top:64px;display:flex;gap:18px;font-size:13.5px}
.nav a{color:var(--ink);text-decoration:none;padding-bottom:4px}
.nav a.active{border-bottom:2px solid var(--ink)}

/* hero */
.hero-accent{left:0;top:575px;width:228px;height:88px;background:var(--sky)}
.hero{left:57px;top:100px;width:1086px;height:540px;background:linear-gradient(120deg,#3b3a33,#5d5a4e 45%,#2f3436)}
.hero h1{position:absolute;left:0;width:100%;top:210px;text-align:center;font-family:var(--serif);font-size:54px;line-height:58px;color:var(--white)}
.dots{position:absolute;left:520px;top:498px;display:flex;gap:8px}
.dots span{width:9px;height:9px;border-radius:50%;background:var(--white)}
.dots span.on{background:none;border:1.5px solid var(--white)}

/* about */
.about-title{left:300px;top:745px;width:288px;text-align:right;font-size:31px}
.about-text{left:220px;top:797px;width:368px;text-align:right;font-size:11.5px;line-height:20.5px;color:var(--muted)}
.about-text p+p{margin-top:20px}
.about-frame{left:640px;top:689px;width:372px;height:377px;background:var(--plum)}
.about-photo{left:632px;top:697px;width:373px;height:377px;background:radial-gradient(circle at 55% 45%,#6b4a36,#b98a6e 55%,#8a97a8)}

/* what we do */
.mist{left:0;top:1138px;width:1200px;height:712px;background:var(--mist)}
.card{position:absolute;width:270px;height:332px;background:var(--white);border:1px solid #9a9aa6;border-radius:6px;text-align:center}
.card .ph{height:197px;border-radius:6px 6px 0 0}
.card h3{font-family:var(--serif);font-size:15.5px;line-height:20px;margin-top:12px}
.card p{font-size:11.5px;line-height:15px;color:var(--muted);margin:6px 30px 0}
.card .btn{left:86px;bottom:-16px;width:100px;height:30px;font-size:13px}
.video{left:173px;top:1739px;width:855px;height:338px;background:linear-gradient(100deg,#7d7d7b,#9d9c97 50%,#6f6f6c);border-radius:4px}
.video h3{position:absolute;top:120px;width:100%;text-align:center;font-family:var(--serif);font-size:30px;color:var(--white);font-weight:700}
.play{position:absolute;left:408px;top:168px}

/* services */
.service{position:absolute;top:2133px;width:143px;height:115px;background:var(--white);box-shadow:0 2px 10px rgba(0,0,0,.07);text-align:center}
.service svg{margin-top:22px}
.service span{display:block;margin-top:8px;font-family:var(--serif);font-weight:700;font-size:16px}

/* partner */
.partner{left:0;top:2300px;width:1200px;height:159px;background:linear-gradient(90deg,var(--plum) 0,var(--plum-deep) 100%)}
.jar{left:612px;top:2300px;width:157px;height:159px;background:linear-gradient(#6a6372,#8d8791)}
.partner-kicker{left:170px;top:2330px;font-family:var(--serif);font-weight:700;font-size:15px;color:var(--white)}
.partner-title{left:170px;top:2360px;font-family:var(--serif);font-size:30px;line-height:35px;color:var(--white);font-weight:700}
.make{left:866px;top:2358px;width:161px;height:43px;background:var(--white);color:var(--ink);font-weight:600;font-size:14px;border-radius:10px}

/* news */
.news{position:absolute;top:2554px;width:271px;text-align:center}
.news .ph{height:216px}
.news h3{font-family:var(--serif);font-size:16.5px;margin-top:22px}
.news p{font-size:13px;line-height:19px;color:var(--muted);margin:14px 28px 0}
.news .btn{position:relative;margin:12px auto 0;width:100px;height:29px;font-size:13px}
.arrow{position:absolute;top:2706px;width:38px;height:37px;background:var(--plum);display:flex;align-items:center;justify-content:center}

/* feed */
.email{left:408px;top:3045px;width:251px;height:38px;border:1px solid #888;border-radius:20px;padding-left:16px;display:flex;align-items:center;font-size:13px;color:#888}
.send{left:670px;top:3045px;width:122px;height:38px;gap:14px}

/* footer */
.footer{left:0;top:3122px;width:1200px;height:236px;background:linear-gradient(#3b3634,#2c2826)}
.fcol{position:absolute;top:3152px;color:var(--white)}
.fcol h4{font-family:var(--serif);font-size:16px;margin-bottom:10px}
.fcol li{list-style:none;font-size:11px;line-height:20px}
.fcol.tight li{line-height:16px}
.frule{left:173px;top:3300px;width:855px;height:1px;background:#8a8480}
.copy{left:0;top:3322px;width:1200px;text-align:center;font-size:11px;color:var(--white)}
</style>
</head>
<body>

<header>
  <div class="abs header-block"></div>
  <div class="abs brand"><span class="brand-dot"></span>Lanternfield Collective</div>
  <a class="btn donate" href="#">Donate Now</a>
  <nav class="abs nav">
    <a class="active" href="#">Home</a><a href="#">About Us</a><a href="#">Projects</a><a href="#">What We Do</a><a href="#">Media</a><a href="#">Contact Us</a>
  </nav>
</header>

<section>
  <div class="abs hero-accent"></div>
  <div class="abs hero" role="img" aria-label="Volunteer handing food parcels to a family">
    <h1>Helping the needy<br>Christian families</h1>
    <div class="dots"><span class="on"></span><span></span><span></span></div>
  </div>
</section>

<section>
  <h2 class="abs about-title">About Us</h2>
  <div class="abs about-text">
    <p>Lorem ipsum dolor sit amet, ei quo tollit incorrupte, audire comprehensam his cu. Te vel scribentur deterruisset, eu veniam labore doctus sit. Suavitate tincidunt pri no, pro docendi interesset ei. Ex est persecuti deterruisset. dque dicta blandit te eum,</p>
    <p>Te mel homero equidem denique, vix an putent adversarium. Cu his falli dolores partiendo. An vivendo maluisset mei. An ius liber ubique ocurreret, epicurei theophrastus an ius.</p>
  </div>
  <a class="btn" href="#" style="left:302px;top:973px;width:135px;height:37px">Read More</a>
  <a class="btn btn-outline" href="#" style="left:452px;top:973px;width:134px;height:37px">Contact Us</a>
  <div class="abs about-frame"></div>
  <div class="abs about-photo" role="img" aria-label="Cupped hands holding soil with a seedling"></div>
</section>

<section>
  <div class="abs mist"></div>
  <h2 class="section-title" style="top:1178px">What We Do</h2>
  <div class="card" style="left:173px;top:1242px">
    <div class="ph" role="img" aria-label="Two smiling children outdoors" style="background:linear-gradient(135deg,#5a4b3e,#3c4f7a)"></div>
    <h3>Lorem Ipsum Dolor<br>Sit Amet</h3>
    <p>pro docendi interesset ei. Ex est persecuti deterruisset. dque dicta esset ei Ex est.</p>
    <a class="btn" href="#">Read More</a>
  </div>
  <div class="card" style="left:465px;top:1265px">
    <div class="ph" role="img" aria-label="Plate of food being served" style="background:linear-gradient(135deg,#6d5a40,#c8b89a 55%,#8a8a86)"></div>
    <h3>Lorem Ipsum Dolor<br>Sit Amet</h3>
    <p>pro docendi interesset ei. Ex est persecuti deterruisset. dque dicta esset ei Ex est.</p>
    <a class="btn" href="#">Read More</a>
  </div>
  <div class="card" style="left:757px;top:1242px">
    <div class="ph" role="img" aria-label="Group reading together at a table" style="background:linear-gradient(135deg,#9a8878,#5a6a86 60%,#2e2e35)"></div>
    <h3>Lorem Ipsum Dolor<br>Sit Amet</h3>
    <p>pro docendi interesset ei. Ex est persecuti deterruisset. dque dicta esset ei Ex est.</p>
    <a class="btn" href="#">Read More</a>
  </div>
  <a class="btn" href="#" style="left:533px;top:1646px;width:134px;height:36px">View More</a>

  <div class="abs video" role="img" aria-label="Volunteers in grey shirts at a community event">
    <h3>WATCH OUR LATEST ACTIVITIES</h3>
    <svg class="play" width="46" height="46" viewBox="0 0 46 46"><circle cx="23" cy="23" r="22" fill="#fff"/><path d="M17 13l15 10-15 10z" fill="#3a3a3a"/></svg>
  </div>
</section>

<section>
  <div class="service" style="left:198px">
    <svg width="44" height="44" viewBox="0 0 44 44" fill="none" stroke="#333" stroke-width="2"><rect x="8" y="14" width="16" height="28" rx="4" transform="rotate(40 22 22)"/><path d="M30 6l8 7M26 10l6 5"/></svg>
    <span>Pure Water</span>
  </div>
  <div class="service" style="left:418px">
    <svg width="44" height="44" viewBox="0 0 44 44" fill="none" stroke="#333" stroke-width="2"><circle cx="22" cy="22" r="19"/><circle cx="22" cy="22" r="12"/><path d="M17 13v18M27 13v18M15 13v6M19 13v6"/></svg>
    <span>Healthy Food</span>
  </div>
  <div class="service" style="left:637px">
    <svg width="44" height="44" viewBox="0 0 44 44" fill="none" stroke="#333" stroke-width="2"><rect x="6" y="10" width="22" height="12" rx="6" transform="rotate(-40 17 16)"/><circle cx="28" cy="29" r="11"/><path d="M17 29h22"/></svg>
    <span>Medication</span>
  </div>
  <div class="service" style="left:856px">
    <svg width="48" height="44" viewBox="0 0 48 44" fill="none" stroke="#333" stroke-width="2"><path d="M24 10v28M24 10C18 6 10 6 4 8v28c6-2 14-2 20 2 6-4 14-4 20-2V8c-6-2-14-2-20 2z"/></svg>
    <span>Education</span>
  </div>
</section>

<section>
  <div class="abs partner"></div>
  <div class="abs jar" role="img" aria-label="Glass donation jar"></div>
  <p class="abs partner-kicker">Get Started Now</p>
  <h2 class="abs partner-title">BE A PART OF<br>THE PROUD PARTNER.</h2>
  <a class="btn make" href="#">Make A Donation</a>
</section>

<section>
  <h2 class="section-title" style="top:2492px">News &amp; Updates</h2>
  <div class="arrow" style="left:60px"><svg width="14" height="20" viewBox="0 0 14 20"><path d="M11 2L3 10l8 8" fill="none" stroke="#fff" stroke-width="2.5"/></svg></div>
  <div class="arrow" style="left:1102px"><svg width="14" height="20" viewBox="0 0 14 20"><path d="M3 2l8 8-8 8" fill="none" stroke="#fff" stroke-width="2.5"/></svg></div>
  <article class="news" style="left:173px">
    <div class="ph" role="img" aria-label="Girl wearing a headscarf" style="background:linear-gradient(135deg,#23322e,#3e5a54 60%,#2a3432)"></div>
    <h3>Lorem Ipsum Dolor</h3>
    <p>Per inceptos himenaeos. Mauris in erat justo. Nullam ac urna eu felis dapibus.</p>
    <a class="btn" href="#">Read More</a>
  </article>
  <article class="news" style="left:465px">
    <div class="ph" role="img" aria-label="Three young children standing together" style="background:linear-gradient(135deg,#7d7560,#a89a84 50%,#6a5e50)"></div>
    <h3>Lorem Ipsum Dolor</h3>
    <p>Per inceptos himenaeos. Mauris in erat justo. Nullam ac urna eu felis dapibus.</p>
    <a class="btn" href="#">Read More</a>
  </article>
  <article class="news" style="left:757px">
    <div class="ph" role="img" aria-label="Child drinking water from a tap" style="background:linear-gradient(135deg,#6a8a5c,#9cb28a 50%,#5c6e8c)"></div>
    <h3>Lorem Ipsum Dolor</h3>
    <p>Per inceptos himenaeos. Mauris in erat justo. Nullam ac urna eu felis dapibus.</p>
    <a class="btn" href="#">Read More</a>
  </article>
</section>

<section>
  <h2 class="section-title" style="top:2980px">Get Every Single Feeds</h2>
  <div class="abs email">Your Email Address*</div>
  <a class="btn send" href="#">SEND <svg width="22" height="18" viewBox="0 0 22 18"><path d="M1 8L21 1l-5 16-5-6z" fill="#fff"/></svg></a>
</section>

<footer>
  <div class="abs footer" role="img" aria-label="Wooden letter blocks spelling a donation message"></div>
  <div class="fcol" style="left:173px"><h4>Useful Links</h4><ul><li>Home</li><li>About</li><li>What We Do</li><li>Contact</li></ul></div>
  <div class="fcol" style="left:393px"><h4>Quick Links</h4><ul><li>Tearms &amp; Conditions</li><li>Privacy Policy</li><li>Blogs</li><li>Projects</li></ul></div>
  <div class="fcol tight" style="left:612px"><h4>Address</h4><ul><li>48 Orchard Lane,</li><li>Fairhaven, Country</li><li>PO Box 30918</li></ul></div>
  <div class="fcol tight" style="left:833px"><h4>Phone</h4><ul><li>555-014-2318</li><li>555-014-2318</li></ul></div>
  <div class="abs frule"></div>
  <div class="abs copy">© 2019 All Rights Reserved. Lanternfield Collective.</div>
</footer>

</body>
</html>
```